Project Management - Web Design Project

Valtrix 4 Management Limited is a company which provides specialist Project Control and Contract Management expertise to the Engineering, Construction and Manufacturing industries. The emphasis is on advanced Project Management techniques in particular Planning & Scheduling, Cost Control, Change Control, Risk Management, Reporting and Contract Administration. We are a global company (albeit a small start-up at this time) and pride ourselves on our ability to support projects to help them achieve their goals and objectives. Our aim is to implement work class control tools in a simple and user friendly manner. We would like the website to appear professional but at the same time easy to navigate and a good balance between text and pictures. The final design should communicate our value added service to our customers, our willingness to support and our structured approach to our work.

Target Market(s)

Project Management professionals working for engineering, construction and manufacturing organisations involved with delivering projects.

Industry/Entity Type

Construction

Requirements
Must have
• The website must include all of the content from the attached Excel brief. The company logo (attached) must also be included in the design. The design must portray a professional look and feel. Please include pictures and photographs related to project management in the engineering, construction and manufacturing industries. We may supplement with pictures of our own during the next steps.
Nice to have
• Emphasis that Valtrix 4 is available to support, guide, direct to achieve positive outcomes for the projects. We work hard at developing our customer relationships. Our employees are experienced in advanced project management techniques.
Should not have
• The design should not use old style fonts. It should look modern and professional. Do not include cartoons or silly illustrations.

```html
<!DOCTYPE html>
<html lang="en">
<head>
<meta charset="utf-8">
<title>Valtrix 4 Management Limited</title>
<link href="https://fonts.googleapis.com/css2?family=Questrial&family=Roboto+Condensed:ital,wght@0,700;1,400&family=Montserrat:wght@700&display=swap" rel="stylesheet">
<style>
  :root {
    --page: #f6f6f6;
    --dark: #262626;
    --dark-line: #3a3a3a;
    --blue: #1a6fd0;
    --grey-head: #9a9a9a;
    --text: #333333;
    --muted: #8a8a8a;
    --light-text: #c9c9c9;
    --orange: #c8501e;
    --nav-text: #a8a8a8;
  }
  * { box-sizing: border-box; margin: 0; padding: 0; }
  html, body { width: 879px; height: 1200px; overflow: hidden; background: var(--page); }
  body { position: relative; font-family: "Questrial", sans-serif; color: var(--text); }

  .brand { position: absolute; left: 73px; top: 12px; width: 150px; text-align: center; }
  .brand-mark { width: 66px; height: 66px; border-radius: 50%; background: var(--blue); margin: 0 auto 8px; }
  .brand-name { font-size: 17px; letter-spacing: 2px; color: #555; line-height: 1.1; text-transform: uppercase; }
  .brand-name small { display: block; font-size: 9px; letter-spacing: 1.6px; }

  .account-link { position: absolute; left: 724px; top: 26px; font-size: 10px; color: #555; }

  .main-nav { position: absolute; left: 34px; top: 141px; width: 811px; height: 72px; background: var(--dark); display: flex; border-bottom: 2px solid #444; }
  .main-nav a { display: flex; align-items: center; justify-content: center; height: 100%; font-size: 11px; color: var(--nav-text); text-decoration: none; text-transform: uppercase; letter-spacing: -0.2px; border-right: 2px solid #1a1a1a; }
  .main-nav a:last-child { border-right: none; }
  .main-nav a.is-active { color: var(--blue); }

  .hero-visual { position: absolute; left: 362px; top: 232px; width: 475px; height: 324px; z-index: 0; background: radial-gradient(ellipse at 55% 50%, #d9cdbd 0%, #e9e6e1 45%, var(--page) 75%); }
  .hero-title { position: absolute; z-index: 2; left: 72px; top: 306px; font-family: "Montserrat", sans-serif; font-weight: 700; line-height: 1; }
  .hero-title .line-1 { display: block; font-size: 53px; color: var(--grey-head); letter-spacing: 1px; }
  .hero-title .line-2 { display: block; font-size: 38px; color: var(--blue); letter-spacing: 0.5px; margin-top: 3px; }
  .hero-tagline { position: absolute; z-index: 2; left: 72px; top: 462px; font-family: "Roboto Condensed", sans-serif; font-style: italic; font-size: 19px; color: var(--orange); white-space: nowrap; }
  .slider-dots { position: absolute; z-index: 2; left: 385px; top: 538px; display: flex; gap: 6px; }
  .slider-dots span { width: 17px; height: 17px; border-radius: 50%; background: radial-gradient(circle at 35% 30%, #dcdcdc, #8c8c8c); }
  .slider-dots span.is-current { background: radial-gradient(circle at 35% 30%, #5aa7ff, #0c5cc2); }

  .admin-col { position: absolute; top: 581px; width: 330px; }
  .admin-col h2 { font-weight: 400; font-size: 22px; color: #333; margin-left: 1px; }
  .step { position: relative; height: 73px; padding-left: 57px; font-size: 11.5px; line-height: 17px; letter-spacing: 0.3px; }
  .step:first-of-type { margin-top: 23px; }
  .step-num { position: absolute; left: 0; top: 2px; width: 43px; height: 43px; border-radius: 50%; background: var(--dark); color: #fff; font-family: "Roboto Condensed", sans-serif; font-size: 48px; line-height: 43px; text-align: right; padding-right: 1px; overflow: hidden; }
  .step strong { display: block; font-weight: 700; font-family: "Questrial", sans-serif; }
  .more-link { display: inline-block; margin-left: 57px; font-family: "Roboto Condensed", sans-serif; font-weight: 700; font-size: 21px; letter-spacing: 1px; color: #4a4a4a; text-decoration: none; }
  .more-link span { font-family: "Questrial", sans-serif; font-weight: 400; font-size: 13px; vertical-align: 3px; }

  .feature-band { position: absolute; left: 34px; top: 899px; width: 811px; height: 285px; background: var(--dark); }
  .feature-band .rule { position: absolute; left: 0; right: 0; top: 62px; height: 1px; background: #444; }
  .feature-band .rule.bottom { top: 259px; }
  .feature { position: absolute; top: 0; width: 212px; }
  .feature h3 { font-weight: 400; font-size: 28px; color: var(--blue); height: 62px; line-height: 62px; }
  .feature .lead { margin-top: 16px; width: 205px; font-size: 11.5px; font-weight: 700; line-height: 17px; color: #bdbdbd; letter-spacing: 0.3px; }
  .feature p { margin-top: 14px; font-size: 11.5px; line-height: 17.3px; color: var(--light-text); letter-spacing: 0.3px; }
  .feature .more-link { margin: 14px 0 0; color: #6e6e6e; }
  .copyright { position: absolute; left: 29px; top: 266px; font-size: 10px; color: var(--muted); letter-spacing: 0.3px; }
</style>
</head>
<body>
  <header>
    <div class="brand">
      <div class="brand-mark"></div>
      <div class="brand-name">Valtrix 4<small>Management Limited</small></div>
    </div>
    <a class="account-link">Login or Register</a>
    <nav class="main-nav">
      <a class="is-active" style="width:110px">Home</a>
      <a style="width:112px">About</a>
      <a style="width:173px">Prime Contract</a>
      <a style="width:162px">Sub Contract</a>
      <a style="width:121px">Clients</a>
      <a style="width:133px">Contact</a>
    </nav>
  </header>

  <section class="hero">
    <div class="hero-visual" role="img" aria-label="House under construction resting on rolled architectural plans with sketched dimension lines"></div>
    <h1 class="hero-title"><span class="line-1">PROJECT</span><span class="line-2">CONTROL</span></h1>
    <p class="hero-tagline">CONTRACT MANAGEMENT EXPERTISE</p>
    <div class="slider-dots"><span></span><span class="is-current"></span><span></span><span></span><span></span></div>
  </section>

  <section class="admin-col" style="left:86px">
    <h2>Prime Contract Administration</h2>
    <div class="step"><div class="step-num">1</div><strong>Ea prompta conceptam</strong>Cu nec velit postea<br>tincidunt, ei sea electram</div>
    <div class="step"><div class="step-num">2</div><strong>Ea prompta conceptam</strong>Cu nec velit postea<br>tincidunt, ei sea electram</div>
    <div class="step"><div class="step-num">3</div><strong>Ea prompta conceptam</strong>Cu nec velit postea<br>tincidunt, ei sea electram</div>
    <a class="more-link">MORE <span>&gt;</span></a>
  </section>

  <section class="admin-col" style="left:499px">
    <h2>Sub Contract Administration</h2>
    <div class="step"><div class="step-num">1</div><strong>Ea prompta conceptam</strong>Cu nec velit postea<br>tincidunt, ei sea electram</div>
    <div class="step"><div class="step-num">2</div><strong>Ea prompta conceptam</strong>Cu nec velit postea<br>tincidunt, ei sea electram</div>
    <div class="step"><div class="step-num">3</div><strong>Ea prompta conceptam</strong>Cu nec velit postea<br>tincidunt, ei sea electram</div>
    <a class="more-link">MORE <span>&gt;</span></a>
  </section>

  <footer class="feature-band">
    <div class="rule"></div>
    <div class="feature" style="left:28px">
      <h3>Aeterno</h3>
      <div class="lead">Ea prompta conceptam maiestatis eum. Mei illud intellegam</div>
      <p>Cu nec velit postea tincidunt, ei sea electram dissentiet, vis at fugit putent tritani. Ius ea quod accusamus laboramus, sea id facilis</p>
      <a class="more-link">MORE <span>&gt;</span></a>
    </div>
    <div class="feature" style="left:294px">
      <h3>Nusquam</h3>
      <div class="lead">Ea prompta conceptam maiestatis eum. Mei illud intellegam</div>
      <p>Cu nec velit postea tincidunt, ei sea electram dissentiet, vis at fugit putent tritani. Ius ea quod accusamus laboramus, sea id facilis</p>
      <a class="more-link">MORE <span>&gt;</span></a>
    </div>
    <div class="feature" style="left:563px">
      <h3>Concept</h3>
      <div class="lead">Ea prompta conceptam maiestatis eum. Mei illud intellegam</div>
      <p>Cu nec velit postea tincidunt, ei sea electram dissentiet, vis at fugit putent tritani. Ius ea quod accusamus laboramus, sea id facilis</p>
      <a class="more-link">MORE <span>&gt;</span></a>
    </div>
    <div class="rule bottom"></div>
    <div class="copyright">Copyright © Valtrix 4 Management Limited</div>
  </footer>
</body>
</html>
```